Flyer for Clothing Line Launch Event

I need a flyer designed for the launch of my women's clothing line in February 2016. I will need to use this flyer on my website, social media and print.

The Collections

Our contemporary collections are comprised of influences drawing from bohemian and chic motifs. The term "Bohemian" is described as "simply an artist or littérateur who, consciously or unconsciously, secedes from conventionality in life and in art". "Chic" was borrowed from the French in the late 19th century and has come to mean stylish or elegant.

About my company:

We design free and romantic garments targeted to fashion-forward women driven by uniqueness and desire to accentuate her confidence and class through style. We look forward to our clients indulging in the LorettaVance brand to include our Keystone Circle, Lend-A-Heart, eNewsletters, Trunk Shows and Fashion Shows.

Target Market(s)

upscale women ages 30-50

Industry/Entity Type

Fashion

Font styles to use
Decorative
Script
Other font styles liked:
• Handwritten type script

Colors
000000
f37122
3377b5
e667a6

Requirements
Must have
• colors similar to my website boutique.lorettavance-example.com
• my logo
Nice to have
• image from my website
• my logo

```html
<!DOCTYPE html>
<html lang="en">
<head>
<meta charset="utf-8">
<title>LorettaVance Boutique – Collection Launch Soiree</title>
<link href="https://fonts.googleapis.com/css2?family=Josefin+Sans:wght@300;400;600&family=Pinyon+Script&display=swap" rel="stylesheet">
<style>
  :root {
    --ink: #000000;
    --night: #0b0b0c;
    --copper: #d98a4e;
    --copper-light: #f0a868;
    --copper-deep: #b8652c;
    --ivory: #f2ece6;
    --violet: #5a5478;
    --violet-deep: #2c2838;
  }
  * { margin: 0; padding: 0; box-sizing: border-box; }
  html, body { width: 847px; height: 1200px; overflow: hidden; background: var(--ink); }
  .flyer {
    position: relative;
    width: 847px;
    height: 1200px;
    overflow: hidden;
    background: radial-gradient(ellipse at 40% 35%, #1a1a1c 0%, var(--night) 55%, var(--ink) 100%);
    font-family: "Josefin Sans", sans-serif;
    color: var(--copper);
  }
  .model-photo {
    position: absolute;
    left: 60px;
    top: 95px;
    width: 420px;
    height: 730px;
    background:
      radial-gradient(ellipse 26% 13% at 48% 12%, rgba(150,120,110,0.5), transparent 70%),
      radial-gradient(ellipse 50% 52% at 48% 58%, var(--violet) 0%, var(--violet-deep) 55%, transparent 85%);
  }
  .centered {
    position: absolute;
    text-align: center;
    white-space: nowrap;
  }
  .eyebrow {
    left: 460px; width: 334px; top: 153px;
    font-weight: 300; font-size: 20px; letter-spacing: 9px; padding-left: 9px;
  }
  .boutique-mark { left: 460px; width: 334px; top: 252px; }
  .boutique-mark .dot {
    display: inline-block; width: 40px; height: 40px;
    border-radius: 50%; border: 2px solid var(--copper);
  }
  .boutique-mark .name {
    display: block; margin-top: 12px;
    font-size: 24px; font-weight: 400; letter-spacing: 1px;
  }
  .boutique-mark .sub {
    display: block; margin-top: 6px;
    font-size: 16px; font-weight: 300; letter-spacing: 8px; padding-left: 8px;
  }
  .invite-line {
    font-weight: 300; font-size: 22px; letter-spacing: 8px; padding-left: 8px;
  }
  .join { left: 450px; width: 334px; top: 496px; }
  .designer-label { left: 460px; width: 334px; top: 553px; }
  .designer-name {
    left: 99px; width: 700px; top: 585px;
    font-size: 46px; font-weight: 600; letter-spacing: 9px; padding-left: 9px;
    background: linear-gradient(180deg, var(--copper-light) 0%, var(--copper-deep) 100%);
    -webkit-background-clip: text; background-clip: text;
    -webkit-text-fill-color: transparent;
  }
  .launch-line { left: 92px; width: 700px; top: 666px; }
  .event-title {
    left: 87px; width: 700px; top: 745px;
    font-family: "Pinyon Script", cursive;
    font-weight: 400; font-size: 135px; line-height: 1;
    letter-spacing: 34px; padding-left: 34px;
    color: var(--copper-deep);
  }
  .swash { position: absolute; left: 165px; top: 900px; }
  .highlights {
    left: 129px; width: 700px; top: 992px;
    list-style: none; color: var(--ivory);
    font-weight: 300; font-size: 25px; letter-spacing: 10px; padding-left: 10px;
    line-height: 40px;
  }
</style>
</head>
<body>
  <main class="flyer">
    <div class="model-photo" role="img" aria-label="Photo of the designer wearing a high-neck violet tie-dye dress"></div>

    <p class="centered eyebrow">INTRODUCING</p>

    <div class="centered boutique-mark">
      <span class="dot"></span>
      <span class="name">LORETTAVANCE</span>
      <span class="sub">BOUTIQUE</span>
    </div>

    <p class="centered invite-line join">PLEASE JOIN</p>
    <p class="centered invite-line designer-label">DESIGNER</p>
    <p class="centered designer-name">LORETTA VANCE</p>
    <p class="centered invite-line launch-line">FOR HER COLLECTION LAUNCH</p>

    <h1 class="centered event-title">Soiree</h1>

    <svg class="swash" width="530" height="40" viewBox="0 0 530 40" aria-hidden="true">
      <path d="M5 12 Q265 -4 525 12 Q265 4 5 12 Z" fill="var(--copper-deep)"/>
      <path d="M30 32 Q265 14 500 32" stroke="var(--copper-deep)" stroke-width="2" fill="none"/>
    </svg>

    <ul class="centered highlights">
      <li>RUNWAY SHOW</li>
      <li>SHOPPING</li>
      <li>LITE BITES &amp; CHAMPAGNE</li>
    </ul>
  </main>
</body>
</html>
```